Gummy Label design for hemp company

I need a 3.25 inch wide by 4 inch tall label made to be put on bags of gummies. I will include all disclaimers that need to be there, as well as my logo. This is for our 25 mg Delta 8 gummies 20ct, but I will use the design for our entire gummy line, just editing the text. Needs to have ingredient list. Ingredients: Sugar, Inulin, Corn syrup, water, pectin, citric acid, baking soda, fruit, hemp extract.

Everything should be on one label as this is going on a sticker that will be placed on a bag.
I would like to highlight that they are vegan if possible.

• Must have the following disclaimer: "Contains Farm Bill compliant hemp extract. These statements have not been evaluated by the QVR. This product is NOT intended to treat, cure, or prevent any disease. Do not operate heavy machinery while using this product. This product may cause you to fail a drug test. Consult with your doctor before trying any new products. Do not take if pregnant or lactating. If you experience any adverse effects, discontinue use and seek advice from your physician."
• NEEDS TO SAY: "100% hemp derived" also "<.3% D9 THC"

```html
<!DOCTYPE html>
<html lang="en">
<head>
<meta charset="utf-8">
<title>Sunny Leaf Hemp – 25 mg Delta 8 Gummies Label</title>
<link href="https://fonts.googleapis.com/css2?family=Oswald:wght@500;600&family=Noto+Sans:wght@500;800&display=swap" rel="stylesheet">
<style>
  :root {
    --stage: #ece8df;
    --lime: #a9c83c;
    --leaf: #5a9e3a;
    --forest: #2f7a34;
    --deep: #2a6a2c;
    --sun: #f3dc3c;
    --ink: #1b1b1b;
    --white: #ffffff;
  }
  * { margin: 0; padding: 0; box-sizing: border-box; }
  html, body { width: 1200px; height: 675px; overflow: hidden; background: var(--stage); }
  .label {
    position: absolute; left: 305px; top: 0;
    width: 590px; height: 675px; overflow: hidden;
    background: linear-gradient(90deg, var(--lime) 0%, var(--leaf) 45%, var(--forest) 100%);
  }
  .label__shapes { position: absolute; inset: 0; width: 590px; height: 675px; }
  .brand {
    position: absolute; left: 0; width: 590px; top: 150px;
    text-align: center;
    font-family: "Noto Sans", sans-serif; font-weight: 800;
    font-size: 46px; line-height: 1; color: var(--deep); letter-spacing: -0.5px;
  }
  .brand__dot {
    position: absolute; left: 270px; top: 72px;
    width: 50px; height: 50px; border-radius: 50%; background: var(--leaf);
  }
  .product-title {
    position: absolute; left: 0; width: 590px; top: 318px;
    text-align: center;
    font-family: "Oswald", sans-serif; font-weight: 500;
    font-size: 25px; letter-spacing: 3px; color: var(--white);
  }
  .disclaimer {
    position: absolute; left: 67px; top: 362px; width: 470px;
    font-family: "Noto Sans", sans-serif; font-weight: 500;
    font-size: 13.4px; line-height: 17px; color: var(--ink);
  }
  .claims {
    position: absolute; left: 0; width: 590px; top: 484px;
    text-align: center;
    font-family: "Oswald", sans-serif; font-weight: 600;
    font-size: 29px; line-height: 31px; color: var(--deep);
  }
  .ingredients__heading {
    position: absolute; left: 203px; top: 569px; width: 158px; height: 37px;
    border: 2px solid var(--deep); border-radius: 3px;
    background: var(--lime);
    font-family: "Oswald", sans-serif; font-weight: 600;
    font-size: 26px; line-height: 32px; text-align: center; color: var(--ink);
  }
  .ingredients__list {
    position: absolute; left: 45px;
    list-style: none; display: flex; flex-wrap: nowrap;
    font-family: "Oswald", sans-serif; font-weight: 500;
    font-size: 18px; line-height: 22px; color: var(--white);
    white-space: nowrap;
  }
  .ingredients__list--first { top: 613px; width: 500px; justify-content: space-between; }
  .ingredients__list--second { top: 644px; gap: 14px; }
  .ingredients__list li { display: flex; align-items: center; gap: 7px; flex-shrink: 0; }
  .ingredients__list li::before {
    content: ""; flex-shrink: 0; width: 19px; height: 19px; border-radius: 50%; background: var(--white);
  }
</style>
</head>
<body>
<main class="label">
  <svg class="label__shapes" viewBox="0 0 945 1080" preserveAspectRatio="none" aria-hidden="true">
    <defs>
      <linearGradient id="titleBand" x1="0" x2="1" y1="0" y2="0">
        <stop offset="0" stop-color="#a9c83c" stop-opacity="0"/>
        <stop offset="0.2" stop-color="#a9c83c"/>
        <stop offset="0.8" stop-color="#a9c83c"/>
        <stop offset="1" stop-color="#a9c83c" stop-opacity="0"/>
      </linearGradient>
    </defs>
    <rect class="stripe" x="120" y="0" width="110" height="1080" fill="#4f963a"/>
    <rect class="stripe" x="230" y="0" width="40" height="1080" fill="#8fbb3a"/>
    <rect class="stripe" x="270" y="0" width="110" height="1080" fill="#3f8a36" opacity="0.7"/>
    <path class="plaque" fill="#f3dc3c" d="M48,150 Q48,115 85,115 L180,115 Q250,25 472,20 Q695,25 765,115 L860,115 Q895,115 895,150 L895,740 Q895,775 860,795 Q700,900 472,905 Q245,900 85,795 Q48,775 48,740 Z"/>
    <path class="plaque-window" fill="#ffffff" d="M68,165 Q68,135 100,135 L195,135 Q265,50 472,45 Q680,50 750,135 L845,135 Q878,135 878,165 L878,400 Q878,430 848,440 Q700,500 472,502 Q245,500 97,440 Q68,430 68,400 Z"/>
    <rect class="title-band" x="65" y="512" width="815" height="54" fill="url(#titleBand)"/>
  </svg>

  <span class="brand__dot"></span>
  <h1 class="brand">Sunny Leaf Hemp</h1>

  <h2 class="product-title">25 MG DELTA 8 GUMMIES</h2>

  <p class="disclaimer">Contains Farm Bill compliant hemp extract. These statements have not been evaluated by the QVR. This product is NOT intended to treat, cure, or prevent any disease. Do not operate heavy machinery while using this product. This product may cause you to fail a drug test. Consult with your doctor before trying any new products. Do not take if pregnant or lactating. If you experience any adverse effects, discontinue use and seek advice from your physician.</p>

  <p class="claims">100% HEMP DERIVED<br>&lt;.3% D9 THC</p>

  <h3 class="ingredients__heading">INGREDIENTS</h3>
  <ul class="ingredients__list ingredients__list--first">
    <li>SUGAR</li><li>CORN SYRUP</li><li>BAKING SODA</li><li>PECTIN</li><li>FRUIT</li>
  </ul>
  <ul class="ingredients__list ingredients__list--second">
    <li>INULIN</li><li>WATER</li><li>CITRIC ACID</li><li>HEMP EXTRACT</li>
  </ul>
</main>
</body>
</html>
```